Our Family Values Printed on Canvas for our Home

My family has decided on the following values:

Be Grateful
Act Kindly
Stay Honest
Smile Often
Do Your Best
Live Adventurously
Never Stop Learning
Help Others
Love Always

We desire to print a sign (on 16x20 or 20x16 canvas) for various rooms in our house to remind us of the family we want to be. Each value has equal value, and we want the sign to reflect that (for example, we don't want one value to appear larger than another). We are not particular about colors or images however here are some hints about us that may help:
- My wife's favorite color is dark teal
- We live in the Pacific Northwest
- We love nature
- My wife and I have two sons and a dog

We look forward to your design!

--Tobias

Target Market(s)

Our family and friends

Industry/Entity Type

Non-Profit

Font styles to use
Decorative

Requirements
Must have
• - Printable on 16x20 or 20x60 canvas
• - Equal emphasis on each value
• - Easy to read

```html
<!DOCTYPE html>
<html lang="en">
<head>
<meta charset="utf-8">
<title>Family Values Canvas Signs</title>
<link rel="stylesheet" href="https://fonts.googleapis.com/css2?family=Lobster&display=swap">
<style>
  :root {
    --page: #ffffff;
    --teal: #0ae8df;
    --ink: #050505;
    --heart-red: #ff0000;
    --figure-white: rgba(255, 255, 255, 0.55);
  }
  html, body {
    margin: 0;
    padding: 0;
    width: 1200px;
    height: 1200px;
    overflow: hidden;
    background: var(--page);
  }
  .canvas {
    position: relative;
    width: 1200px;
    height: 1200px;
  }
  .sign {
    position: absolute;
    background: var(--teal);
  }
  .sign--portrait {
    left: 68px;
    top: 322px;
    width: 461px;
    height: 576px;
  }
  .sign--landscape {
    left: 575px;
    top: 379px;
    width: 576px;
    height: 461px;
  }
  .values {
    position: absolute;
    margin: 0;
    padding: 0;
    list-style: none;
    font-family: "Lobster", cursive;
    color: var(--ink);
    white-space: nowrap;
    z-index: 2;
  }
  .sign--portrait .values {
    left: 0;
    width: 461px;
    top: 25px;
    text-align: center;
    font-size: 31px;
    line-height: 41px;
  }
  .sign--landscape .values {
    right: 33px;
    top: 18px;
    text-align: right;
    font-size: 36px;
    line-height: 46.5px;
  }
  .heart-art,
  .family-art {
    position: absolute;
    display: block;
    z-index: 1;
  }
  .sign--portrait .heart-art { left: 24px; top: 64px; width: 98px; height: 82px; }
  .sign--landscape .heart-art { left: 127px; top: 47px; width: 172px; height: 146px; }
  .sign--portrait .family-art { left: 26px; top: 406px; width: 404px; height: 150px; }
  .sign--landscape .family-art { left: 23px; top: 307px; width: 310px; height: 133px; }
</style>
</head>
<body>
<main class="canvas">
  <section class="sign sign--portrait">
    <svg class="heart-art" viewBox="0 0 98 82" role="img" aria-label="Red scribbled heart illustration">
      <path d="M49 80 C20 58 2 44 2 24 C2 10 12 2 25 2 C36 2 44 9 49 18 C54 9 62 2 73 2 C86 2 96 10 96 24 C96 44 78 58 49 80 Z" fill="var(--heart-red)"/>
    </svg>
    <ul class="values">
      <li>Be Grateful</li>
      <li>Act Kindly</li>
      <li>Stay Honest</li>
      <li>Smile Often</li>
      <li>Do Your Best</li>
      <li>Live Adventurously</li>
      <li>Never Stop Learning</li>
      <li>Help Others</li>
      <li>Love Always</li>
    </ul>
    <svg class="family-art" viewBox="0 0 404 150" preserveAspectRatio="none" role="img" aria-label="White line drawing of a family of four children-style figures and a dog">
      <rect x="0" y="0" width="404" height="150" rx="12" fill="var(--figure-white)"/>
    </svg>
  </section>

  <section class="sign sign--landscape">
    <svg class="heart-art" viewBox="0 0 98 82" role="img" aria-label="Red scribbled heart illustration">
      <path d="M49 80 C20 58 2 44 2 24 C2 10 12 2 25 2 C36 2 44 9 49 18 C54 9 62 2 73 2 C86 2 96 10 96 24 C96 44 78 58 49 80 Z" fill="var(--heart-red)"/>
    </svg>
    <ul class="values">
      <li>Be Grateful</li>
      <li>Act Kindly</li>
      <li>Stay Honest</li>
      <li>Smile Often</li>
      <li>Do Your Best</li>
      <li>Live Adventurously</li>
      <li>Never Stop Learning</li>
      <li>Help Others</li>
      <li>Love Always</li>
    </ul>
    <svg class="family-art" viewBox="0 0 310 133" role="img" aria-label="White line drawing of a family of four children-style figures and a dog">
      <path d="M10 0 H200 Q210 0 210 10 V46 H300 Q310 46 310 56 V123 Q310 133 300 133 H10 Q0 133 0 123 V10 Q0 0 10 0 Z" fill="var(--figure-white)"/>
    </svg>
  </section>
</main>
</body>
</html>
```